Women Web Portal

We are developing an internet portal with content created by and for women in Latin America.
This portal will contain different categories focused on relevant topics for women who are at the same time mothers, lovers, workers, pet-owners, ...

We are looking for design that are at the same time uncluttered, easy-to-use and obvious, and comfy. Pastel colours, buttons using traditional fonts, large space for pictures, highlighted social elements,...

Our target being the middle-class women, we want a design that feels comfortable, real, a bit trendy and traditional, not a Vestry & Holm design, something women can relate to and feel comfortable enough to come back and participate.

Examples of websites:
www.cookvault.example
dama.portalvix.example
www.cabellorivo.example
www.casserol.example
Updates

Hi dear designers. After viewing some first drafts, I have updated the brief so you might have a better understanding of what we are looking for.

Thanks

Reason: We've been away for a while, unavailable to provide adequate feedback to the designs already sent. So we're extending the deadline in order to give time to everyone to adapt their work according to the feedback we'll be providing today.

Target Market(s)

Women between 25 and 50 years from Latin America. Mainly mothers: basically, we want women to interact with each other and with the content of the site so they create a strong community.

Advertisingly speaking, we want to have users, contents and FMCG brands to live together on this website.

Industry/Entity Type

Internet

Requirements
Must have
• Pastel colours for category tabs. Comfortable look & feel.

The design should include 3 different pages:
- Homepage
- Article page
- User profile

The page will be done in responsive design, so design should be thought to be adapted according to the browser (2 or 3 columns).

Thanks for doing it as a PSD file .

The design should also include:
- 8 category tabs
- Space for 728x90px and 300x600px advertising format.
- A relevant menu bar at the beginning of each page
Nice to have
• News feed/best content/most active comments zone: we need to bring forward content to our users so they'll be attracted to visit more pages of the website.

Small format to register (account).

Slider or any other moving objects.

Any idea that would facilitate and increase user participation
Should not have
• Actual text. please use Lorem Ipsum.

```html
<!DOCTYPE html>
<html lang="es">
<head>
<meta charset="utf-8">
<title>mujerada – perfil de usuaria</title>
<link rel="stylesheet" href="https://fonts.googleapis.com/css2?family=Open+Sans:wght@400;700&display=swap">
<style>
:root{
  --purple:#660099;
  --purple-dot:#7a2bb0;
  --yellow:#ffcc00;
  --green:#33cc33;
  --blue:#6666ee;
  --grey:#7a7a7a;
  --rule:#c8c8c8;
  --strip:#1a1a1a;
  --white:#ffffff;
}
*{box-sizing:border-box;margin:0;padding:0}
html,body{width:878px;height:1200px;overflow:hidden;background:var(--white)}
body{position:relative;font-family:"Open Sans",Verdana,sans-serif;color:var(--purple)}
.abs{position:absolute}

/* header */
.topbar{left:23px;top:0;width:832px;height:43px;background:var(--purple)}
.brand{left:96px;top:5px;color:var(--white);font-size:25px;font-weight:400;letter-spacing:.5px}
.brand-mark{left:30px;top:8px;width:26px;height:26px;border-radius:50%;background:var(--white)}
.login{left:405px;top:13px;color:var(--yellow);font-weight:700;font-size:16px}
.icon{top:5px;width:38px;height:34px}
.social{top:4px;width:36px;height:36px;border-radius:5px;background:var(--yellow)}

.banner{left:23px;top:50px;width:832px;height:103px;
  background:linear-gradient(180deg,#dbe9f2 0%,#9cc2d8 35%,#4f7f5a 55%,#1f8fb8 70%,#0b4f8c 100%)}

/* category nav */
.nav{left:23px;top:167px;width:832px;height:44px;display:flex;gap:3px}
.nav-item{flex:1;border-bottom:2px solid var(--rule);text-align:center;color:var(--grey);font-size:14.5px;line-height:18px}
.nav-dot{display:block;width:13px;height:13px;margin:3px auto 0;border-radius:50%;
  background:radial-gradient(circle at 35% 30%,#e6c8ff,var(--purple-dot) 60%,#3d005c)}
.nav-dot.is-active{background:radial-gradient(circle at 35% 30%,#eaffd0,#8fe04a 60%,#3f9a10)}

/* cards */
.card{border:4px solid var(--purple);border-radius:12px;background:var(--white)}
.card-title{position:absolute;left:15px;top:8px;font-size:24px;font-weight:700}
.t-green{color:var(--green)}
.t-blue{color:var(--blue)}
.figure{position:absolute;border-radius:14px 14px 4px 4px}

.profile{left:25px;top:278px;width:392px;height:225px}
.profile-age{left:15px;top:38px;font-size:13.5px;font-weight:700}
.profile-facts{left:15px;top:68px;font-size:13.5px;font-weight:700;line-height:16.5px}
.profile-facts p{margin-bottom:16px}
.profile-photo{left:254px;top:29px;width:128px;height:119px;background:linear-gradient(160deg,#6b4a34,#c58f6e 55%,#3b2a20)}
.dots{position:absolute;display:flex;gap:15px}
.dots i{width:14px;height:14px;border-radius:50%;background:radial-gradient(circle at 35% 30%,#e6c8ff,var(--purple-dot) 60%,#3d005c)}

.groups{left:463px;top:278px;width:392px;height:225px}
.group-list{left:15px;top:53px;width:230px;font-size:13.5px;font-weight:700;line-height:16.5px}
.group-row{display:flex;justify-content:space-between}

.photos{left:25px;top:571px;width:830px;height:226px}
.strip{left:22px;top:59px;width:781px;height:112px;background:var(--strip)}
.thumb{position:absolute}
.arrow{position:absolute;width:26px;height:30px}

.friends{left:25px;top:862px;width:830px;height:258px}
.friend{position:absolute;top:57px;height:114px}
.friend-name{position:absolute;top:185px;font-size:13.5px;font-weight:700;text-align:center}
</style>
</head>
<body>

<header>
  <div class="abs topbar"></div>
  <div class="abs brand-mark" aria-hidden="true"></div>
  <div class="abs brand">mujerada</div>
  <div class="abs login">login/register</div>
  <svg class="abs icon" style="left:551px" viewBox="0 0 38 34" aria-label="mensajes"><rect x="3" y="5" width="32" height="24" fill="none" stroke="var(--yellow)" stroke-width="3"/><path d="M3 5 L19 19 L35 5 M3 29 L15 16 M35 29 L23 16" fill="none" stroke="var(--yellow)" stroke-width="3"/></svg>
  <svg class="abs icon" style="left:609px" viewBox="0 0 38 34" aria-label="chat"><ellipse cx="14" cy="12" rx="12" ry="9" fill="var(--yellow)"/><path d="M8 19 L5 27 L15 20Z" fill="var(--yellow)"/><ellipse cx="26" cy="20" rx="10" ry="8" fill="var(--yellow)" stroke="var(--purple)" stroke-width="2"/><path d="M30 26 L34 32 L26 27Z" fill="var(--yellow)"/></svg>
  <div class="abs social" style="left:669px" role="img" aria-label="red social"></div>
  <div class="abs social" style="left:724px" role="img" aria-label="red social"></div>
  <svg class="abs icon" style="left:784px" viewBox="0 0 38 34" aria-label="buscar"><circle cx="13" cy="12" r="9" fill="none" stroke="var(--yellow)" stroke-width="4"/><path d="M20 18 L35 30" stroke="var(--yellow)" stroke-width="6" stroke-linecap="round"/></svg>
</header>

<div class="abs banner" role="img" aria-label="Paisaje de costa con mar turquesa y colinas verdes"></div>

<nav class="abs nav">
  <div class="nav-item">home<span class="nav-dot"></span></div>
  <div class="nav-item">article<span class="nav-dot"></span></div>
  <div class="nav-item">lorem<span class="nav-dot"></span></div>
  <div class="nav-item">dolor<span class="nav-dot"></span></div>
  <div class="nav-item">consectetur<span class="nav-dot"></span></div>
  <div class="nav-item">occaecat<span class="nav-dot"></span></div>
  <div class="nav-item">cupidatat<span class="nav-dot"></span></div>
  <div class="nav-item">culpa<span class="nav-dot is-active"></span></div>
</nav>

<section class="abs card profile">
  <div class="figure" style="left:293px;top:-42px;width:40px;height:52px;background:var(--green)" role="img" aria-label="figura de usuaria"></div>
  <h2 class="card-title t-green">Cristina</h2>
  <div class="abs profile-age">28</div>
  <div class="abs profile-facts">
    <p>I live in Kingston Jamaica<br>I am Married<br>I have 2 Children</p>
    <p>Hobies: sailing, photography,<br>cooking, travel</p>
    <p>Occupation housewife</p>
  </div>
  <div class="abs profile-photo" role="img" aria-label="Foto de perfil de Cristina"></div>
  <div class="dots" style="left:287px;top:182px"><i></i><i></i><i></i></div>
</section>

<section class="abs card groups">
  <div class="figure" style="left:212px;top:-42px;width:140px;height:52px;background:linear-gradient(90deg,var(--blue) 33%,var(--green) 33% 66%,var(--blue) 66%)" role="img" aria-label="grupo de usuarias"></div>
  <h2 class="card-title t-blue">Groups</h2>
  <div class="abs group-list">
    <div class="group-row"><span>Cooking</span><span>17 posts</span></div>
    <div class="group-row"><span>Travel</span><span>5 posts</span></div>
    <div class="group-row"><span>Photography</span><span>3 posts</span></div>
  </div>
</section>

<section class="abs card photos">
  <svg class="abs" style="left:677px;top:-23px" width="73" height="46" viewBox="0 0 73 46" aria-label="cámara"><rect x="0" y="0" width="73" height="46" rx="5" fill="var(--green)"/><circle cx="34" cy="23" r="16" fill="var(--blue)"/><rect x="52" y="6" width="14" height="4" fill="var(--white)"/></svg>
  <h2 class="card-title t-green">Photos</h2>
  <div class="abs strip">
    <div class="thumb" style="left:44px;top:26px;width:93px;height:63px;background:linear-gradient(135deg,#3a2a1a,#d04a8a)" role="img" aria-label="foto: mujer en una fiesta"></div>
    <div class="thumb" style="left:164px;top:26px;width:94px;height:63px;background:linear-gradient(135deg,#0a3a10,#3fd060)" role="img" aria-label="foto: baile con luces verdes"></div>
    <div class="thumb" style="left:284px;top:26px;width:95px;height:63px;background:linear-gradient(135deg,#8a4a10,#e08a40)" role="img" aria-label="foto: pista de baile"></div>
    <div class="thumb" style="left:421px;top:13px;width:62px;height:93px;background:linear-gradient(160deg,#b06020,#e0b080)" role="img" aria-label="foto: pareja bailando"></div>
    <div class="thumb" style="left:526px;top:26px;width:95px;height:63px;background:linear-gradient(135deg,#6a3a20,#d09070)" role="img" aria-label="foto: pareja en una celebración"></div>
    <div class="thumb" style="left:647px;top:26px;width:93px;height:63px;background:linear-gradient(135deg,#e6a0b0,#f5d5d5)" role="img" aria-label="foto: retrato de niña"></div>
  </div>
  <svg class="arrow" style="left:18px;top:181px" viewBox="0 0 26 30"><path d="M0 15 L26 0 L26 30Z" fill="var(--green)"/></svg>
  <svg class="arrow" style="left:776px;top:181px" viewBox="0 0 26 30"><path d="M26 15 L0 0 L0 30Z" fill="var(--green)"/></svg>
  <div class="dots" style="left:382px;top:187px"><i></i><i></i><i></i></div>
</section>

<section class="abs card friends">
  <div class="figure" style="left:681px;top:-34px;width:80px;height:52px;background:linear-gradient(90deg,var(--blue) 50%,var(--green) 50%)" role="img" aria-label="pareja de amigas"></div>
  <h2 class="card-title t-blue">Friends</h2>
  <div class="friend" style="left:19px;width:183px;background:linear-gradient(160deg,#8a7a60,#c89a80)" role="img" aria-label="foto de Carmen"></div>
  <div class="friend" style="left:218px;width:109px;background:linear-gradient(160deg,#cfe6f2,#b08060)" role="img" aria-label="foto de Dona"></div>
  <div class="friend" style="left:335px;width:154px;background:linear-gradient(160deg,#e8eef2,#7a4a30)" role="img" aria-label="foto de April"></div>
  <div class="friend" style="left:493px;width:179px;background:linear-gradient(160deg,#2a2020,#c09080)" role="img" aria-label="foto de Consuela"></div>
  <div class="friend" style="left:681px;width:100px;background:linear-gradient(160deg,#3a2a1a,#a07850)" role="img" aria-label="retrato pintado de Zuza"></div>
  <div class="friend-name" style="left:19px;width:183px">Carmen</div>
  <div class="friend-name" style="left:218px;width:109px">Dona</div>
  <div class="friend-name" style="left:335px;width:154px">April</div>
  <div class="friend-name" style="left:493px;width:179px">Consuela</div>
  <div class="friend-name" style="left:681px;width:100px">Zuza</div>
  <svg class="arrow" style="left:18px;top:207px" viewBox="0 0 26 30"><path d="M0 15 L26 0 L26 30Z" fill="var(--blue)"/></svg>
  <svg class="arrow" style="left:776px;top:207px" viewBox="0 0 26 30"><path d="M26 15 L0 0 L0 30Z" fill="var(--blue)"/></svg>
  <div class="dots" style="left:382px;top:218px"><i></i><i></i><i></i></div>
</section>

</body>
</html>
```